'The Willow Lantern Boutique' Ecommerce boutique (womens clothing) needs a business card design

Ecommerce boutique (womens clothing) needs a business card design, we need a business card that's fresh, innovative, clean design that matches our quality products and attracts quality suppliers as well as customers.
We aim to create a feel good shopping experience that goes past the point of sale.
Updates
Target Market(s)
Women 18-35, fashion forward, disposable income, unique.
Industry/Entity Type
Boutique
Font styles to use
Colors
Designer to choose colors to be used in the design.
Look and feel
Each slider illustrates characteristics of the customer's brand and the style your logo design should communicate.

```html
<!DOCTYPE html>
<html lang="en">
<head>
<meta charset="utf-8">
<title>The Willow Lantern Boutique – Business Card</title>
<link rel="stylesheet" href="https://fonts.googleapis.com/css2?family=Cormorant+Garamond:ital,wght@0,500;1,500;1,600&family=Lobster&display=swap">
<style>
  :root {
    --page: #ffffff;
    --card-edge: #c24d9c;
    --card-mid: #d172b1;
    --ink: #ffffff;
    --logo-ink: #111111;
    --rose-light: #eea6d4;
    --rose-deep: #dc86c0;
  }
  * { margin: 0; padding: 0; box-sizing: border-box; }
  html, body {
    width: 1200px; height: 1000px; overflow: hidden;
    background: var(--page);
  }
  .card {
    position: absolute; left: 365px; top: 50px;
    width: 502px; height: 878px;
    background: radial-gradient(ellipse 70% 55% at 50% 42%, var(--card-mid) 0%, var(--card-mid) 35%, var(--card-edge) 100%);
    color: var(--ink);
    overflow: hidden;
  }
  .brand-name {
    position: absolute; left: 0; right: 0; top: 88px;
    text-align: center;
    font-family: "Cormorant Garamond", Georgia, serif;
    font-weight: 500;
    font-size: 40px; line-height: 1.05;
    letter-spacing: 3px;
    color: var(--logo-ink);
    text-transform: uppercase;
  }
  .person { position: absolute; left: 0; right: 0; top: 322px; text-align: center; }
  .person-name {
    font-family: "Lobster", "Brush Script MT", cursive;
    font-size: 46px; line-height: 1;
    letter-spacing: 1px;
  }
  .person-role {
    margin-top: 10px;
    font-family: "Cormorant Garamond", Georgia, serif;
    font-style: italic; font-weight: 500;
    font-size: 29px;
  }
  .contacts {
    position: absolute; left: 45px; top: 555px;
    list-style: none;
    font-family: "Cormorant Garamond", Georgia, serif;
    font-style: italic; font-weight: 600;
    font-size: 25px; line-height: 36px;
  }
  .contacts li { display: flex; align-items: center; white-space: nowrap; }
  .contacts svg { width: 22px; height: 20px; margin-right: 4px; flex: none; }
  .contacts .sep { font-style: normal; margin-right: 6px; }
  .rose {
    position: absolute; left: 176px; top: 682px;
    width: 152px; height: 136px;
    border-radius: 48% 52% 40% 46% / 50% 46% 54% 50%;
    background: radial-gradient(circle at 50% 40%, var(--rose-light) 0%, var(--rose-deep) 80%);
    opacity: 0.75;
  }
</style>
</head>
<body>
  <section class="card">
    <h1 class="brand-name">The Willow Lantern<br>Boutique</h1>

    <div class="person">
      <h2 class="person-name">Maren Ashby</h2>
      <p class="person-role">Founder</p>
    </div>

    <ul class="contacts">
      <li>
        <svg viewBox="0 0 22 20" aria-hidden="true"><path fill="#fff" d="M2 7c0-3 4-4 9-4s9 1 9 4l-3 1-1-2H6L5 8zM6 9h10l3 7H3z"/><circle cx="11" cy="12.5" r="2" fill="#d070b0"/></svg>
        <span class="sep">:</span>0400-555-218
      </li>
      <li>
        <svg viewBox="0 0 22 20" aria-hidden="true"><rect x="2" y="5" width="18" height="11" fill="none" stroke="#fff" stroke-width="2"/><path d="M2 5l9 6 9-6" fill="none" stroke="#fff" stroke-width="2"/></svg>
        <span class="sep">:</span>maren@willowlanternboutique.com.au
      </li>
      <li>
        <svg viewBox="0 0 22 20" aria-hidden="true"><g fill="none" stroke="#fff" stroke-width="1.5"><circle cx="11" cy="10" r="8.5"/><ellipse cx="11" cy="10" rx="3.5" ry="8.5"/><path d="M2.5 10h17M4 5.5h14M4 14.5h14"/></g></svg>
        <span class="sep">:</span>www.thewillowlanternboutique.com
      </li>
    </ul>

    <div class="rose" role="img" aria-label="Faint pale pink rose illustration"></div>
  </section>
</body>
</html>
```